"At last - a professional cleaning company that delivers what it promises; is fussy about the detail

Hi,

We need a A4 flyer desgin for our cleaing comapny, focusing on dry carpet cleaing I attached our catalogue to give some idea. In addition our websites can provide more information.

Our Services:-

General Cleaning

Carry out heavy cleansing tasks and special projects.
Clean, stock and supply designated facility areas (dusting, sweeping, vacuuming, mopping, cleaning ceiling vents, restroom cleaning etc).
Using electrically powered scrubbing and polishing machines to burnish, scrub, polish and spray clean floors.

Window Cleaning

Regular, Reliable Window Cleaning.
Hard To Reach Windows.
Single 7 Multi-Storey.
Frames and Glass Cleaned.

Floor Cleaning Cleaning

Marble Cleaning & Polishing.
Tile & Grout Cleaning.
Hardwood Floors Services.
Vinyl Floors.
Many Thanks,

Target Market(s)

commercial cleaning

Industry/Entity Type

Cleaning Service

Font styles to use
Serif
Sans Serif

Colors
0555a3
9bcb3c
ffffff

Requirements
Must have
• why we are different
Nice to have
• N/A
Should not have
• N/A

```html
<!DOCTYPE html>
<html lang="en">
<head>
<meta charset="utf-8">
<title>Gulfline Cleaning Co. – Dry Carpet Cleaning Flyer</title>
<link rel="stylesheet" href="https://fonts.googleapis.com/css2?family=Josefin+Sans:wght@400;600&family=Josefin+Slab:wght@400;600&display=swap">
<style>
  :root{
    --brand-blue:#0555a3;
    --deep-blue:#0b47a0;
    --sky-blue:#1fa3e8;
    --pale-blue:#dcefff;
    --ink:#1c1c1c;
    --white:#ffffff;
    --backdrop:#e6e6e6;
  }
  *{box-sizing:border-box;margin:0;padding:0}
  html,body{width:684px;height:1200px;overflow:hidden;background:var(--backdrop)}
  .flyer{position:absolute;left:0;top:117px;width:684px;height:966px;background:var(--white);overflow:hidden;
    font-family:"Josefin Slab",Georgia,serif;color:var(--ink)}
  .hero{position:absolute;left:0;top:0;width:684px;height:380px}
  .brand{position:absolute;left:56px;top:288px;width:260px;text-align:center}
  .brand-mark{display:inline-block;width:16px;height:16px;border-radius:50%;background:var(--brand-blue);vertical-align:middle;margin-right:7px}
  .brand-name{font-family:"Josefin Slab",Georgia,serif;font-weight:400;font-size:17px;color:#2a2a2a;vertical-align:middle}
  .brand-since{display:block;margin:8px auto 0;width:90px;border-top:2px solid #777;padding-top:3px;font-size:13px;color:#333}
  .intro-band{position:absolute;left:0;top:376px;width:684px;height:116px;background:var(--deep-blue);color:var(--white);padding:10px 24px 0}
  .band-title{font-size:23px;font-weight:400;display:flex;align-items:center;gap:12px}
  .band-title::after{content:"";flex:1;height:1px;background:var(--white);margin-top:-4px;max-width:380px}
  .band-text{font-family:"Josefin Sans",Arial,sans-serif;font-size:11.4px;line-height:1.42;margin-top:7px}
  .services{position:absolute;left:28px;top:508px;width:440px}
  .section-title{font-size:23px;color:var(--deep-blue);font-weight:400;display:flex;align-items:center;gap:10px}
  .section-title::after{content:"";width:140px;height:1px;background:var(--deep-blue);margin-top:-4px}
  .service{margin-top:10px}
  .service-head{display:flex;align-items:center;gap:8px;font-size:14px;font-weight:400;color:var(--deep-blue)}
  .service-head span{padding-bottom:2px;border-bottom:1px solid var(--deep-blue);min-width:330px}
  .service-icon{width:14px;height:14px;background:var(--ink);border-radius:2px}
  .ticks{list-style:none;margin:7px 0 0 8px;font-size:11.6px;line-height:1.3}
  .ticks li{padding-left:16px;position:relative}
  .ticks li::before{content:"✓";position:absolute;left:0;top:0;font-family:"Josefin Sans",Arial,sans-serif}
  .art{position:absolute;inset:0;width:684px;height:966px;pointer-events:none}
  .footer{position:absolute;left:0;top:916px;width:684px;height:50px;background:var(--deep-blue);color:var(--white);
    display:flex;align-items:center;padding:0 20px 0 30px;font-family:"Josefin Sans",Arial,sans-serif}
  .call{font-size:18px;display:flex;align-items:center;gap:6px}
  .social{display:flex;gap:12px;margin-left:26px}
  .social i{display:block;width:24px;height:24px;border:1.5px solid var(--white);border-radius:50%}
  .web{margin-left:auto;font-size:11px}
</style>
</head>
<body>
<main class="flyer">
  <svg class="hero" viewBox="0 0 684 380">
    <defs>
      <linearGradient id="machinePhoto" x1="0" y1="0" x2="0" y2="1">
        <stop offset="0" stop-color="#3a3a3a"/><stop offset=".55" stop-color="#5a4a3a"/><stop offset="1" stop-color="#d8b98c"/>
      </linearGradient>
      <linearGradient id="roomPhoto" x1="0" y1="0" x2="1" y2="1">
        <stop offset="0" stop-color="#d9d4c8"/><stop offset="1" stop-color="#7b6d78"/>
      </linearGradient>
    </defs>
    <rect x="0" y="0" width="684" height="350" fill="url(#machinePhoto)" role="img" aria-label="Photo of a dry extraction carpet cleaning machine on carpet"/>
    <path d="M0,0 H300 C330,60 345,140 315,195 C290,235 220,250 140,262 L0,285 Z" fill="url(#roomPhoto)" stroke="var(--sky-blue)" stroke-width="5" role="img" aria-label="Photo of a cleaner vacuuming a hotel room"/>
    <path d="M0,282 C100,250 250,222 400,247 C500,265 600,308 684,326 L684,340 C600,322 500,280 400,262 C250,238 100,266 0,300 Z" fill="var(--sky-blue)"/>
    <path d="M0,296 C100,262 250,236 400,259 C500,277 600,320 684,336 L684,354 C600,336 500,292 400,272 C250,248 100,274 0,312 Z" fill="var(--brand-blue)"/>
    <path d="M0,312 C100,274 250,248 400,272 C500,292 600,336 684,354 L684,380 L0,380 Z" fill="var(--white)"/>
  </svg>

  <div class="brand">
    <span class="brand-mark"></span><span class="brand-name">Gulfline Cleaning Co.</span>
    <span class="brand-since">Since 1989</span>
  </div>

  <section class="intro-band">
    <h1 class="band-title">Dry Carpet Cleaning</h1>
    <p class="band-text">The TERRA Dry Extraction Carpet Cleaning System is the environmentally preferred carpet cleaning system that deep cleans your carpet and reduces dust mites and moulds leaving it fresh, clean, dry and back in use immediately. Made from 100% plant-based resources and a little bit of water, TERRA is the easy, effective, safe and green carpet cleaner. All our TERRA Carpet Cleaning Systems are available throughout the Qatar. Green, Clean, Dry Immediately.</p>
  </section>

  <svg class="art" viewBox="0 0 684 966">
    <rect x="470" y="520" width="214" height="390" rx="40" fill="#cfe6fb" role="img" aria-label="Illustration of a cleaning lady with a mop and a bucket of supplies"/>
    <path d="M0,905 C200,850 420,850 684,820 L684,916 L0,916 Z" fill="var(--pale-blue)"/>
    <path d="M0,916 C220,860 440,860 684,835 L684,848 C440,872 220,872 0,930 Z" fill="var(--brand-blue)"/>
    <circle cx="414" cy="768" r="76" fill="#9fd18a" stroke="var(--white)" stroke-width="4" role="img" aria-label="Photo of a uniformed cleaner wiping a window"/>
    <circle cx="414" cy="768" r="80" fill="none" stroke="var(--sky-blue)" stroke-width="3"/>
    <circle cx="313" cy="833" r="61" fill="#b9d3e2" stroke="var(--white)" stroke-width="4" role="img" aria-label="Photo of a cleaner mopping an office floor"/>
    <circle cx="313" cy="833" r="65" fill="none" stroke="var(--sky-blue)" stroke-width="3"/>
  </svg>

  <section class="services">
    <h2 class="section-title">Our Services</h2>
    <div class="service">
      <h3 class="service-head"><i class="service-icon"></i><span>General Cleaning</span></h3>
      <ul class="ticks">
        <li>Carry out heavy cleansing tasks and special projects.</li>
        <li>Clean, stock and supply designated facility areas (dusting, sweeping, vacuuming, mopping, cleaning ceiling vents, restroom cleaning etc).</li>
        <li>Using electrically powered scrubbing and polishing machines to burnish, scrub, polish and spray clean floors.</li>
      </ul>
    </div>
    <div class="service">
      <h3 class="service-head"><i class="service-icon"></i><span>Window Cleaning</span></h3>
      <ul class="ticks">
        <li>Regular, Reliable Window Cleaning.</li>
        <li>Hard To Reach Windows.</li>
        <li>Single 7 Multi-Storey.</li>
        <li>Frames and Glass Cleaned.</li>
      </ul>
    </div>
    <div class="service">
      <h3 class="service-head"><i class="service-icon"></i><span>Floor Cleaning</span></h3>
      <ul class="ticks">
        <li>Marble Cleaning &amp; Polishing.</li>
        <li>Tile &amp; Grout Cleaning.</li>
        <li>Hardwood Floors Services.</li>
        <li>Vinyl Floors.</li>
      </ul>
    </div>
  </section>

  <footer class="footer">
    <div class="call">Call Now
      <svg width="18" height="18" viewBox="0 0 24 24" aria-hidden="true"><circle cx="12" cy="12" r="10.5" fill="none" stroke="#fff" stroke-width="1.8"/><path d="M8.5 6.5l2 2.5-1.2 1.4c.8 1.7 2 2.9 3.7 3.7l1.4-1.2 2.5 2-1.3 1.8C11 16.5 7.5 13 6.7 7.8z" fill="#fff"/></svg>
      +974 4000 1258</div>
    <div class="social"><i></i><i></i><i></i><i></i></div>
    <div class="web">www.gulflinecleaningco.com</div>
  </footer>
</main>
</body>
</html>
```